Business Card Design Project

Industry/Entity Type

Business

Contact Information for Business Card

The Harlow Vale Gospel Choir
Dean Marsell, Minister of Music

The Coastal Wesleyan Church of Bramford Hill
Founded 1868

Twitter @thehvgc
Instagram harlowvalegc
Facebook facebook.com/hvgc408
Website: harlowvalegc-example.org
For Bookings: (555) 204-HVGC
4287 Bramwell Street, Linwood Falls, PA 19874

Back of the Card
Music and Cd's Recordings Available On
Choirs Website and Also
Tunevox, Orbala Sound, Disc Sprout (the music online logo)

```html
<!DOCTYPE html>
<html lang="en">
<head>
<meta charset="utf-8">
<title>The Harlow Vale Gospel Choir – Business Card</title>
<link rel="stylesheet" href="https://fonts.googleapis.com/css2?family=Roboto:wght@400;500;700&family=Libre+Baskerville:ital@1&display=swap">
<style>
  :root {
    --bg: #e9e6e1;
    --card: #ffffff;
    --red: #c8252f;
    --red-light: #d8444c;
    --blue: #2a66b0;
    --grey: #555555;
    --crest-a: #8a7a3a;
    --crest-b: #b9b9b9;
    --pill-border: #6a9ad6;
  }
  * { box-sizing: border-box; margin: 0; padding: 0; }
  html, body { width: 1200px; height: 911px; overflow: hidden; }
  body { background: var(--bg); font-family: "Roboto", Arial, sans-serif; position: relative; }

  .card {
    position: absolute;
    background: var(--card);
    border-radius: 22px;
    box-shadow: 0 8px 24px rgba(0,0,0,.18);
    overflow: hidden;
  }

  /* Front */
  .card-front { left: 80px; top: 130px; width: 371px; height: 650px; }
  .front-shield { position: absolute; left: 0; top: 0; width: 371px; height: 400px; }
  .front-contact {
    position: absolute; left: 0; top: 36px; width: 100%;
    text-align: center; color: #fff;
  }
  .person-name { font-size: 24px; font-weight: 700; letter-spacing: .5px; }
  .person-title { font-size: 15px; font-weight: 500; margin-bottom: 12px; }
  .contact-item { font-size: 15px; line-height: 1.25; margin-bottom: 3px; }
  .contact-icon { display: block; margin: 0 auto 2px; width: 12px; height: 12px; }
  .crest {
    position: absolute; left: 140px; top: 420px; width: 92px; height: 100px;
    background: linear-gradient(135deg, var(--crest-a), var(--crest-b));
    border-radius: 8px 8px 46px 46px;
  }
  .front-org { position: absolute; left: 0; top: 540px; width: 100%; text-align: center; }
  .choir-name { font-family: "Libre Baskerville", Georgia, serif; font-style: italic; color: var(--red); font-size: 19px; }
  .minister { color: var(--blue); font-weight: 700; font-size: 15px; margin-top: 4px; }
  .church { color: var(--grey); font-size: 11.5px; margin-top: 3px; }
  .founded { color: var(--grey); font-size: 11.5px; }

  /* Back */
  .card-back { left: 510px; top: 300px; width: 620px; height: 354px; }
  .card-back .crest { left: 262px; top: 40px; width: 96px; height: 104px; }
  .back-text {
    position: absolute; left: 0; top: 162px; width: 100%; text-align: center;
    font-family: "Libre Baskerville", Georgia, serif; font-style: italic;
    color: var(--red); font-size: 18px; line-height: 1.45;
  }
  .stores { position: absolute; left: 0; top: 250px; width: 100%; display: flex; justify-content: center; gap: 18px; }
  .store {
    display: flex; align-items: center; gap: 7px;
    border: 1.5px solid var(--pill-border); border-radius: 18px;
    padding: 7px 16px; font-size: 13px; font-weight: 500; color: #222;
  }
  .store-dot { width: 9px; height: 9px; border-radius: 50%; background: #222; }
</style>
</head>
<body>

<section class="card card-front">
  <svg class="front-shield" viewBox="0 0 371 400" aria-hidden="true">
    <defs>
      <linearGradient id="redFill" x1="0" y1="0" x2="1" y2="1">
        <stop offset="0" stop-color="#d8444c"/>
        <stop offset="1" stop-color="#c8252f"/>
      </linearGradient>
    </defs>
    <path d="M0 0 H371 V150 C371 260 300 340 185 396 C70 340 0 260 0 150 Z" fill="#2a66b0"/>
    <path d="M0 0 H371 V146 C371 252 298 330 185 388 C72 330 0 252 0 146 Z" fill="url(#redFill)"/>
  </svg>

  <div class="front-contact">
    <div class="person-name">EVAN CARLOW</div>
    <div class="person-title">CEO/FOUNDER</div>
    <svg class="contact-icon" viewBox="0 0 12 12"><circle cx="6" cy="6" r="5" fill="#fff"/></svg>
    <div class="contact-item">@thehvgc</div>
    <svg class="contact-icon" viewBox="0 0 12 12"><circle cx="6" cy="6" r="5" fill="#fff"/></svg>
    <div class="contact-item">harlowvalegc</div>
    <svg class="contact-icon" viewBox="0 0 12 12"><circle cx="6" cy="6" r="5" fill="#fff"/></svg>
    <div class="contact-item">/hvgc408</div>
    <svg class="contact-icon" viewBox="0 0 12 12"><path d="M2.5 1 L4.5 1 L5.3 3.4 L4 4.4 C4.7 6 6 7.3 7.6 8 L8.6 6.7 L11 7.5 L11 9.5 C11 10.3 10.3 11 9.5 11 C5 11 1 7 1 2.5 C1 1.7 1.7 1 2.5 1 Z" fill="#fff"/></svg>
    <div class="contact-item">(555) 204-HVGC (Bookings)</div>
    <svg class="contact-icon" viewBox="0 0 12 12"><circle cx="6" cy="6" r="5" fill="none" stroke="#fff" stroke-width="1.6"/><path d="M1 6 H11 M6 1 C3.5 3.5 3.5 8.5 6 11 C8.5 8.5 8.5 3.5 6 1" fill="none" stroke="#fff" stroke-width="1"/></svg>
    <div class="contact-item">www.harlowvalegc-example.org</div>
    <svg class="contact-icon" viewBox="0 0 12 12"><path d="M6 11.5 C3 7.5 2 6 2 4.3 A4 4 0 0 1 10 4.3 C10 6 9 7.5 6 11.5 Z" fill="#fff"/><circle cx="6" cy="4.3" r="1.5" fill="#c8252f"/></svg>
    <div class="contact-item">4287 Bramwell Street<br>Linwood Falls, PA 19874</div>
  </div>

  <div class="crest" role="img" aria-label="Choir crest emblem"></div>

  <div class="front-org">
    <div class="choir-name">The Harlow Vale Gospel Choir</div>
    <div class="minister">Dean Marsell, Minister of Music</div>
    <div class="church">The Coastal Wesleyan Church of Bramford Hill</div>
    <div class="founded">Founded 1868</div>
  </div>
</section>

<section class="card card-back">
  <div class="crest" role="img" aria-label="Choir crest emblem"></div>
  <p class="back-text">Music and Cd's Recordings Available On<br>Choirs Website and Also</p>
  <div class="stores">
    <span class="store"><span class="store-dot"></span>Tunevox</span>
    <span class="store"><span class="store-dot"></span>Orbala Sound</span>
    <span class="store"><span class="store-dot"></span>Disc Sprout</span>
  </div>
</section>

</body>
</html>
```